Stationery Design Project

KT7 Staffing requires letterhead and business card designs for a company based in London. Just like the name, we're a management resourcing company, providing resources to third party companies. You can see www.kt7staffing-example.com for ideas on existing colour schemes and design concepts that have been implimented and agreed to. Ultimately the design should broadcast professionalism, safety and the concept of growth.

Target Market(s)

Financial institutes; friendly societies (All UK based)

Industry/Entity Type

Safety

Requirements
Must have
• Files produced should be print ready; and the text in them editable (eg address, name etc)

```html
<!DOCTYPE html>
<html lang="en">
<head>
<meta charset="utf-8">
<title>KT7 Staffing — Stationery</title>
<link rel="stylesheet" href="https://fonts.googleapis.com/css2?family=Fondamento&family=Kalam:wght@700&family=Lobster+Two:ital,wght@1,700&family=Nunito:wght@800&display=swap">
<style>
  :root {
    --ink: #000000;
    --paper: #ffffff;
    --paper-soft: #f5f5f5;
    --paper-fleck: rgba(0, 0, 0, 0.035);
    --teal: #2597a8;
    --teal-light: #6fbcd2;
    --teal-deep: #1e8497;
    --teal-shade: #14606d;
    --teal-glow: #5cc3d3;
    --plate: #2c2f31;
    --plate-light: #6a6d70;
    --label: #222222;
  }
  html, body {
    margin: 0;
    padding: 0;
    overflow: hidden;
    background: var(--paper);
  }
  .canvas {
    position: relative;
    width: 1200px;
    height: 900px;
    overflow: hidden;
    background: var(--paper);
    font-family: "Fondamento", serif;
  }
  .sheet-label {
    position: absolute;
    margin: 0;
    color: var(--label);
    font-family: "Fondamento", serif;
    font-weight: 400;
    text-align: center;
  }
  .sheet-label--card-front { left: 160px; top: 30px; width: 200px; font-size: 12px; }
  .sheet-label--card-back { left: 164px; top: 316px; width: 200px; font-size: 12px; }
  .sheet-label--letterhead { left: 756px; top: 27px; width: 200px; font-size: 17px; }

  /* Shared paper stock */
  .paper-stock {
    background-color: var(--paper-soft);
    background-image:
      repeating-linear-gradient(0deg, var(--paper-fleck) 0 1px, transparent 1px 5px),
      repeating-linear-gradient(90deg, rgba(255,255,255,0.6) 0 3px, transparent 3px 11px),
      repeating-linear-gradient(90deg, var(--paper-fleck) 0 1px, transparent 1px 23px),
      radial-gradient(ellipse at 30% 20%, #fbfbfb 0%, #f1f1f1 100%);
  }

  /* Business card — front */
  .card-front {
    position: absolute;
    left: 10px;
    top: 56px;
    width: 521px;
    height: 255px;
    background: var(--ink);
  }
  .card-front__plate {
    position: absolute;
    left: 108px;
    top: 81px;
    width: 292px;
    height: 96px;
    box-sizing: border-box;
    border: 8px solid var(--teal);
    border-radius: 16px 10px 18px 12px;
    background:
      linear-gradient(90deg, transparent 0 38%, rgba(160,163,166,0.55) 40%, rgba(120,123,126,0.6) 100%),
      repeating-linear-gradient(35deg, rgba(255,255,255,0.06) 0 3px, transparent 3px 9px),
      repeating-linear-gradient(-50deg, rgba(0,0,0,0.25) 0 2px, transparent 2px 8px),
      radial-gradient(ellipse at 50% 40%, var(--plate-light) 0%, var(--plate) 80%);
    box-shadow:
      inset 0 3px 3px var(--teal-glow),
      inset 0 -3px 4px var(--teal-shade),
      inset 0 0 14px rgba(0,0,0,0.75),
      0 0 0 1px var(--teal-shade),
      0 4px 10px rgba(37,151,168,0.25);
    display: flex;
    align-items: center;
    justify-content: center;
    gap: 12px;
  }
  .brand-mark {
    width: 14px;
    height: 14px;
    background: var(--teal-light);
  }
  .brand-name {
    margin: 0;
    font-family: "Nunito", sans-serif;
    font-weight: 800;
    color: var(--teal-light);
    letter-spacing: 0.02em;
  }
  .card-front .brand-name { font-size: 26px; }

  /* Business card — back */
  .card-back {
    position: absolute;
    left: 10px;
    top: 331px;
    width: 521px;
    height: 227px;
  }
  .card-back__name {
    position: absolute;
    left: 47px;
    top: 24px;
    margin: 0;
    font-family: "Kalam", cursive;
    font-weight: 700;
    font-size: 22px;
    color: var(--teal-light);
  }
  .card-back__name-lead { color: var(--teal-deep); }
  .card-back__role {
    position: absolute;
    left: 47px;
    top: 51px;
    margin: 0;
    font-family: "Nunito", sans-serif;
    font-weight: 800;
    font-size: 13px;
    letter-spacing: 0.03em;
    color: var(--ink);
  }
  .card-back__band {
    position: absolute;
    left: 0;
    bottom: 0;
    width: 521px;
    height: 59px;
    background: var(--ink);
  }
  .card-back__contact {
    position: absolute;
    left: 320px;
    top: 1px;
    margin: 0;
    font-family: "Lobster Two", cursive;
    font-style: italic;
    font-weight: 700;
    font-size: 17px;
    line-height: 18.5px;
    letter-spacing: 0.06em;
    color: var(--teal);
  }

  /* Letterhead */
  .letterhead {
    position: absolute;
    left: 550px;
    top: 57px;
    width: 645px;
    height: 798px;
  }
  .letterhead__header {
    position: absolute;
    left: 3px;
    top: 0;
    width: 639px;
    height: 111px;
    background: var(--ink);
    border-radius: 3px;
  }
  .letterhead__brand {
    position: absolute;
    left: 20px;
    top: 28px;
    display: flex;
    align-items: center;
    gap: 8px;
  }
  .letterhead .brand-name { font-size: 18px; }
  .letterhead__sender {
    position: absolute;
    left: 386px;
    top: 31px;
    margin: 0;
    color: var(--teal);
    font-family: "Lobster Two", cursive;
    font-style: italic;
    font-weight: 700;
  }
  .letterhead__sender-name { display: block; font-size: 18px; line-height: 22px; letter-spacing: 0.05em; }
  .letterhead__sender-line { display: block; font-size: 10px; line-height: 11px; letter-spacing: 0.05em; }
  .letterhead__rule {
    position: absolute;
    left: 28px;
    top: 111px;
    width: 5px;
    height: 674px;
    background: var(--teal);
  }
  .letterhead__date {
    position: absolute;
    left: 445px;
    top: 124px;
    margin: 0;
    font-family: "Fondamento", serif;
    font-size: 17px;
    color: var(--label);
    display: flex;
    align-items: baseline;
  }
  .letterhead__date-line {
    display: inline-block;
    width: 88px;
    margin-left: 2px;
    border-bottom: 1px solid var(--label);
  }
</style>
</head>
<body>
<main class="canvas">
  <h2 class="sheet-label sheet-label--card-front">card front</h2>
  <section class="card-front" aria-label="Business card front">
    <div class="card-front__plate">
      <span class="brand-mark"></span>
      <p class="brand-name">KT7 Staffing</p>
    </div>
  </section>

  <h2 class="sheet-label sheet-label--card-back">card back</h2>
  <section class="card-back paper-stock" aria-label="Business card back">
    <p class="card-back__name"><span class="card-back__name-lead">Name o</span>f the person</p>
    <p class="card-back__role">Designation</p>
    <div class="card-back__band">
      <p class="card-back__contact">Contact:<br>Address<br>Phone &amp; Email</p>
    </div>
  </section>

  <h2 class="sheet-label sheet-label--letterhead">letter head design</h2>
  <section class="letterhead paper-stock" aria-label="Letterhead">
    <header class="letterhead__header">
      <div class="letterhead__brand">
        <span class="brand-mark"></span>
        <p class="brand-name">KT7 Staffing</p>
      </div>
      <p class="letterhead__sender">
        <span class="letterhead__sender-name">Name of the person if any</span>
        <span class="letterhead__sender-line">Address</span>
        <span class="letterhead__sender-line">Contact</span>
      </p>
    </header>
    <div class="letterhead__rule"></div>
    <p class="letterhead__date">Date :<span class="letterhead__date-line"></span></p>
  </section>
</main>
</body>
</html>
```